Bright Arch Group business card

Bright Arch Group is the parent company of Bright Arch Building, Bright Arch Plumbing and Bright Arch Renovating. We require a sophisticated business card that covers all aspects of the building and plumbing space without using told or construction items.

Industry/Entity Type

Construction Company

Contact Information for Business Card

Warrick Hadley
Director
0455921834
warrick@brightarch.com.au
Www.brightarch.com.au

Font styles to use
Serif
Sans Serif

Colors
3176b5
ffce3e
0692cd
34a7d8
fbee3e
faa54b

Requirements
Must have
• Logo on front
• Logo and details on rear.
Nice to have
• Maybe water mark or shadow effect with logo
Should not have
• Tools or any construction associated items

```html
<!DOCTYPE html>
<html lang="en">
<head>
<meta charset="utf-8">
<title>Bright Arch Group – Business Card</title>
<link rel="stylesheet" href="https://fonts.googleapis.com/css2?family=Bebas+Neue&family=Josefin+Sans:wght@300&family=Lato:wght@400&display=swap">
<style>
  :root {
    --stage: #e9e6e2;
    --card-dark: #050505;
    --card-light: #ffffff;
    --accent: #f58220;
    --ink: #1a1a1a;
    --muted: #6b6b6b;
    --rule: #9a9a9a;
    --on-dark: #ffffff;
  }
  * { box-sizing: border-box; margin: 0; padding: 0; }
  html, body { width: 1200px; height: 723px; overflow: hidden; }
  body {
    background: var(--stage);
    display: flex;
    align-items: center;
    justify-content: center;
    gap: 70px;
    font-family: "Lato", sans-serif;
  }

  /* Front of card */
  .card-front {
    position: relative;
    width: 560px;
    height: 320px;
    background: var(--card-dark);
    box-shadow: 0 12px 30px rgba(0,0,0,.25);
    display: flex;
    flex-direction: column;
    align-items: center;
    justify-content: center;
  }
  .wordmark {
    display: flex;
    flex-direction: column;
    align-items: center;
    font-family: "Josefin Sans", sans-serif;
    font-weight: 300;
    text-transform: uppercase;
    line-height: 1;
  }
  .wordmark-row { display: flex; align-items: center; gap: 14px; }
  .wordmark-dot {
    width: 14px; height: 14px; border-radius: 50%;
    background: var(--accent);
  }
  .wordmark-name { letter-spacing: .32em; }
  .wordmark-sub { letter-spacing: .55em; margin-top: 10px; }

  .card-front .wordmark { color: var(--on-dark); }
  .card-front .wordmark-name { font-size: 40px; }
  .card-front .wordmark-sub { font-size: 24px; }
  .front-web {
    margin-top: 34px;
    color: var(--on-dark);
    font-size: 14px;
    letter-spacing: .18em;
  }

  /* Back of card */
  .card-back {
    position: relative;
    width: 340px;
    height: 560px;
    background: var(--card-light);
    box-shadow: 0 12px 30px rgba(0,0,0,.2);
    padding: 56px 34px 0 44px;
  }
  .card-back .wordmark { color: var(--ink); align-items: flex-start; }
  .card-back .wordmark-name { font-size: 25px; letter-spacing: .24em; }
  .card-back .wordmark-sub { font-size: 17px; margin-left: 30px; }

  .edge-tab {
    position: absolute;
    left: 0; top: 300px;
    width: 20px; height: 44px;
    background: var(--accent);
    border-radius: 0 22px 22px 0;
  }
  .holder { position: absolute; left: 44px; top: 300px; right: 34px; }
  .holder-name {
    font-family: "Bebas Neue", sans-serif;
    color: var(--accent);
    font-size: 32px;
    letter-spacing: .01em;
    line-height: 1;
  }
  .holder-role { color: var(--muted); font-size: 18px; margin-top: 2px; }
  .holder-rule { border: 0; border-top: 1px solid var(--rule); margin: 22px 0 18px; }

  .contact-list { list-style: none; }
  .contact-item {
    display: flex; align-items: center; gap: 12px;
    color: var(--muted); font-size: 15px; margin-bottom: 9px;
  }
  .contact-icon {
    width: 18px; height: 18px; border-radius: 4px;
    background: var(--accent);
    display: flex; align-items: center; justify-content: center;
    flex: none;
  }
  .contact-icon svg { width: 12px; height: 12px; }
</style>
</head>
<body>

<section class="card-front" aria-label="Card front">
  <div class="wordmark">
    <div class="wordmark-row">
      <span class="wordmark-dot"></span>
      <span class="wordmark-name">Bright Arch</span>
    </div>
    <span class="wordmark-sub">-Group-</span>
  </div>
  <p class="front-web">www.brightarch.com.au</p>
</section>

<section class="card-back" aria-label="Card back">
  <div class="wordmark">
    <div class="wordmark-row">
      <span class="wordmark-name">Bright Arch</span>
      <span class="wordmark-dot"></span>
    </div>
    <span class="wordmark-sub">-Group-</span>
  </div>

  <span class="edge-tab"></span>

  <div class="holder">
    <h1 class="holder-name">Warrick Hadley</h1>
    <p class="holder-role">Director</p>
    <hr class="holder-rule">
    <ul class="contact-list">
      <li class="contact-item">
        <span class="contact-icon">
          <svg viewBox="0 0 12 12"><path d="M3 1l2 2.5-1 1.2a6 6 0 0 0 3.3 3.3l1.2-1L11 9l-1 2C5 11 1 7 1 2z" fill="#fff"/></svg>
        </span>
        0455921834
      </li>
      <li class="contact-item">
        <span class="contact-icon">
          <svg viewBox="0 0 12 12"><rect x="1" y="2.5" width="10" height="7" fill="none" stroke="#fff" stroke-width="1.2"/><path d="M1 2.5l5 4 5-4" fill="none" stroke="#fff" stroke-width="1.2"/></svg>
        </span>
        warrick@brightarch.com.au
      </li>
      <li class="contact-item">
        <span class="contact-icon">
          <svg viewBox="0 0 12 12"><circle cx="6" cy="6" r="4.6" fill="none" stroke="#fff" stroke-width="1.1"/><ellipse cx="6" cy="6" rx="2" ry="4.6" fill="none" stroke="#fff" stroke-width="1"/><path d="M1.4 6h9.2" stroke="#fff" stroke-width="1"/></svg>
        </span>
        www.brightarch.com.au
      </li>
    </ul>
  </div>
</section>

</body>
</html>
```